Heating & Air Conditioning, indoor air quality service and repair company van wrap

Need a well designed van wrap, we are the new company in town so we would like to include our logo that we have which you can refer to logo design files and als800 the colors and fonts. We have a penguin coming out of igloo with sunglassw on . Inerds to have logo, the website, and Heating Air Conditioning, indoor Air Quality Experts. Thank you and we are considering trying to have the penguin a mascot i. Future, Excited to see what van wrap designs come in

Target Market(s)

Residential home owners for in home service repair and install5

Requirements
Must have
• The vehicles will be-** 2021 Torvik LX 3400 with high roof
I attached some examples of the van in pictures

Logo with the penguin, color theme consisyent with logo, although I do like the one of the 4 , in which the color theme was with the penguin white, also like the others . The igloo

Our phone number ( ) - our website with possibly a qr code somewhere
This is also important to feature is our services - Heating , Air Conditioning, Indoor Air Quality Solutions, Water
Filtration - Service , Repairs, Installations, Design Consults
Slogans - if you can work in - Providing Professional Expertise In A Cool Friendly Manner or Bringing Comfort From Our Home To Yours!
A Call to Action- Call Us Today or Go To Our Online Booking

```html
<!DOCTYPE html>
<html lang="en">
<head>
<meta charset="utf-8">
<title>Northpeak Air Co. – Van Wrap Side Panel</title>
<link href="https://fonts.googleapis.com/css2?family=Roboto+Condensed:wght@700&family=Lobster&family=Orbitron:wght@800&display=swap" rel="stylesheet">
<style>
  :root {
    --wrap-orange: #e2673a;
    --accent-yellow: #f1c21b;
    --brand-blue: #2f6fb7;
    --deep-blue: #1f5fc4;
    --navy: #233955;
    --panel-white: #f7f8f9;
    --page-bg: #ffffff;
  }
  * { margin: 0; padding: 0; box-sizing: border-box; }
  html, body {
    width: 1200px; height: 1200px; overflow: hidden;
    background: var(--page-bg);
  }
  .canvas { position: relative; width: 1200px; height: 1200px; }
  .wrap-panel {
    position: absolute; left: 50px; top: 380px;
    width: 1100px; height: 440px;
    border-radius: 18px; overflow: hidden;
    box-shadow: 0 2px 10px rgba(0,0,0,0.12);
  }
  .wrap-shapes { position: absolute; inset: 0; }
  .brand-name {
    position: absolute; left: 764px; top: 150px; transform: translateX(-50%);
    font-family: "Roboto Condensed", sans-serif; font-weight: 700;
    font-size: 54px; line-height: 64px; color: var(--navy); white-space: nowrap;
  }
  .service-list {
    position: absolute; left: 764px; top: 240px; transform: translateX(-50%);
    font-family: "Roboto Condensed", sans-serif; font-weight: 700;
    font-size: 15px; color: var(--brand-blue); text-align: center; line-height: 21px;
    white-space: nowrap;
  }
  .service-list .dot { color: var(--navy); padding: 0 3px; }
  .call-band {
    position: absolute; left: 330px; top: 292px; width: 380px; height: 62px;
    background: linear-gradient(90deg, var(--brand-blue) 0%, var(--brand-blue) 45%, rgba(47,111,183,0) 100%);
  }
  .call-cta {
    position: absolute; left: 395px; top: 286px;
    font-family: "Lobster", cursive; font-size: 22px; line-height: 28px; color: var(--accent-yellow);
  }
  .call-phone {
    position: absolute; left: 394px; top: 318px;
    font-family: "Orbitron", sans-serif; font-weight: 800; font-size: 26px; line-height: 32px;
    color: var(--wrap-orange); letter-spacing: 2px; white-space: nowrap;
  }
  .mascot {
    position: absolute; left: 726px; top: 296px; width: 44px; height: 112px;
    border-radius: 22px 22px 10px 10px;
    background: linear-gradient(180deg, var(--brand-blue), var(--navy));
  }
  .slogan {
    position: absolute; left: 540px; top: 368px; transform: translateX(-50%);
    font-family: "Roboto Condensed", sans-serif; font-weight: 700;
    font-size: 14px; color: var(--navy); text-align: center; line-height: 19px; white-space: nowrap;
  }
</style>
</head>
<body>
<main class="canvas">
  <section class="wrap-panel" aria-label="Van side wrap layout">
    <svg class="wrap-shapes" width="1100" height="440" viewBox="0 0 1100 440" aria-hidden="true">
      <rect class="base-white" width="1100" height="440" fill="var(--panel-white)"/>
      <polygon class="orange-field" points="0,0 706,0 269,440 0,440" fill="var(--wrap-orange)"/>
      <polygon class="yellow-stripe" points="706,0 722,0 285,440 269,440" fill="var(--accent-yellow)"/>
      <polygon class="navy-stripe" points="1100,168 1100,177 868,440 856,440" fill="var(--navy)"/>
      <polygon class="blue-field" points="1100,177 1100,440 868,440" fill="var(--deep-blue)"/>
    </svg>

    <div class="brand-name">NORTHPEAK AIR CO.</div>

    <div class="service-list">
      Air Conditioning<span class="dot">•</span>Heating<span class="dot">•</span>Indoor Air Quality Solutions<span class="dot">•</span>Service<br>
      Water Filtration<span class="dot">•</span>Repair<span class="dot">•</span>Installations<span class="dot">•</span>Design Consults
    </div>

    <div class="call-band"></div>
    <div class="call-cta">Call Us Today!</div>
    <div class="call-phone">435-555-0142</div>

    <div class="mascot" role="img" aria-label="Penguin mascot wearing sunglasses"></div>

    <p class="slogan">
      Providing Professional Expertise In Cool Friendly<br>
      Manner or Bringing Comfort From Our Home To Yours!
    </p>
  </section>
</main>
</body>
</html>
```